Kavro Global Stationery & Logo Design

We are looking for a logo and stationary design for our business, which should include:
1) Letterhead
2) Business cards
3) A4 folders for company marketing materials
4) Envelops and
5) A4 file covers
We are international business consultants and tax advisers. We help companies with entering new markets by developing a market entry strategy, finding business partners and providing cross borders tax and finance advice.
We operate in the United Kingdom, Poland and India. Our target market includes middle and large companies from these three countries.
Company Name: Kavro Global Ltd.
Address: 12 Brackwell Row, Tanhurst, London, EC1V 4QT,
email: hello@kavroglobal.example
Website: www.kavroglobal.example
Phone: +44 (0) 20 3918 4462
Company Slogan: Clear Answers for a Busy Planet
Vision: To be the first choice for clients by delivering exceptional service through innovation and excellence
Mission: To persevere and achieve excellence in our endeavours through simplicity, respect and creativity
Values: Delivering Innovation with Creativity, Integrity, Achieving Excellence, Fun and Respect and Giving Back to Society.
Project Specification
Our preferred colour is royal blue however, we are open to ideas. We would like a design that is elegant but innovative, sleek and modern. The message we would like to convey is that we are professional and trustworthy business partners.
Please do not use Times New Roman or similar fonts.
Logo
The name of the company is Kavro Global Ltd and the logo can only include the company name although we would prefer to use only ‘Kavro Global’ without ‘Ltd’. Kavro does not need to be in capital letters.
Business Cards
Double sided business cards for our British, Polish and Indian office. The addresses should be as follows:
Kavro Global Ltd
12 Brackwell Row, Tanhurst, London, EC1V 4QT, email: name@kavroglobal.example, www.kavroglobal.example, +44 (0) 20 3918 4462
Kavro Global (Poland) sp. z o.o.
ul. Lipowska 38 lok. 214, 00-812 Warszawa, name@kavroglobal.example, www.kavroglobal.example
+48 (0) 22 415 6039
Kavro Global (India) Pvt. Ltd.
Trade Plaza, 29 Harimohan Lane, 3rd Floor, Kolkata, 700 046, name@kavroglobal.example, www.kavroglobal.example
+91 (0) 33 2871 9043
The names and email addresses will be confirmed once a winning design has been selected.
The business cards should include the company slogan and QR code.
Letterhead
All three addresses need to be on the letterhead. Email address should be hello@kavroglobal.example. Design of continuation sheets should be different to the front page.
A4 folders
We would like the outer and inside pages to have a slightly different design. The company slogan, vision, mission and the three offices’ addresses should also come somewhere on the folder. We do not want the design to include too many photos and would be happy with a design which does not have them at all but any other graphics are fine.
A4 file covers
We would need a front, back and side page. Company slogan and the three offices’ addresses should be included.
Envelopes
Window and regular DL and A4 envelopes.
Updates
Project Deadline Extended
Reason: The proposals we have received so far are not in line with our expectations so we would like to give the designer a bit more time to prepare a few new looks. Also, what we have received so far are only logos and the remaining items in our brief have not been prepared yet.

```html
<!DOCTYPE html>
<html lang="en">
<head>
<meta charset="utf-8">
<title>Kavro Global Stationery</title>
<link href="https://fonts.googleapis.com/css2?family=Open+Sans:wght@400;600;700&display=swap" rel="stylesheet">
<style>
  :root{
    --stage:#cbcbcb;
    --paper:#ffffff;
    --navy:#1f2f6b;
    --blue:#0c80d2;
    --ink:#2a2a2a;
    --muted:#6d6f78;
    --rule:#8a8a8a;
  }
  *{box-sizing:border-box;margin:0;padding:0}
  html,body{width:1200px;height:640px;overflow:hidden}
  body{background:var(--stage);font-family:"Open Sans",Arial,sans-serif;color:var(--ink);position:relative}
  .sheet{position:absolute;background:var(--paper);box-shadow:2px 3px 5px rgba(0,0,0,.28);overflow:hidden}
  .sheet svg.art{position:absolute;left:0;top:0;display:block}

  .brand{position:absolute;text-align:left;line-height:1}
  .brand-name{font-weight:700;color:var(--navy);letter-spacing:.2px;white-space:nowrap}
  .brand-tag{color:var(--muted);text-transform:uppercase;letter-spacing:.4px;white-space:nowrap;margin-top:3px}
  .brand-address{color:var(--navy);white-space:nowrap;margin-top:4px}

  /* Letterhead */
  .letterhead{left:30px;top:38px;width:380px;height:537px}
  .letterhead .brand{right:36px;top:26px;text-align:right}
  .letterhead .brand-name{font-size:21px}
  .letterhead .brand-tag{font-size:5px}
  .letter-body{position:absolute;left:38px;top:94px;width:310px;font-size:7.1px;line-height:13.2px}
  .letter-body p{margin-bottom:13.2px}
  .letter-body .opening{margin-bottom:13.2px}
  .signature{width:96px;height:26px;margin:-4px 0 4px 0;background:linear-gradient(90deg,rgba(20,20,20,.12),rgba(20,20,20,.04));border-radius:12px}
  .letter-footer{position:absolute;left:0;bottom:0;width:100%;height:27px;background:var(--navy);border-top:2px solid var(--blue);display:flex;justify-content:center;align-items:center}
  .office{color:#fff;font-size:4.4px;line-height:6.4px;padding:0 12px;white-space:nowrap}
  .office + .office{border-left:0.8px solid rgba(255,255,255,.8)}

  /* Envelopes */
  .envelope{width:352px;height:157px}
  .envelope-front-top{left:438px;top:122px}
  .envelope-front-side{left:822px;top:122px}
  .envelope-back-plain{left:438px;top:347px}
  .envelope-back-navy{left:821px;top:347px}
  .envelope-front-top .brand{left:19px;top:110px}
  .envelope-front-side .brand{left:29px;top:12px}
  .envelope .brand-name{font-size:11.5px}
  .envelope .brand-tag{font-size:3.1px;margin-top:2px}
  .envelope .brand-address{font-size:3.4px;margin-top:3px}
  .flap-mark{position:absolute;left:0;width:100%;top:13px;text-align:center;font-weight:700;font-size:12px;line-height:1}
  .envelope-back-plain .flap-mark{color:var(--navy)}
  .envelope-back-navy .flap-mark{color:#fff}
</style>
</head>
<body>

<section class="sheet letterhead">
  <svg class="art" width="380" height="64" viewBox="0 0 475 80" aria-hidden="true">
    <path d="M0 0H475V27C380 15 250 12 120 22C70 26 30 32 0 38Z" fill="var(--navy)"/>
    <path d="M0 42C60 30 150 21 268 17C160 26 60 46 0 64Z" fill="var(--blue)"/>
  </svg>
  <div class="brand">
    <div class="brand-name">Kavro Global</div>
    <div class="brand-tag">Clear Answers for a Busy Planet</div>
  </div>
  <div class="letter-body">
    <p class="opening">Lorem Ipsum is simply</p>
    <p>&nbsp;dummy text of the printing and typesetting industry. Lorem Ipsum has been the industry's standard dummy text ever since the 1500s, when an unknown printer took a galley of type and scrambled it to make a type specimen book. It has survived not only five centuries, but also the leap into electronic typesetting, remaining essentially unchanged. It was popularised in the 1960s with the release of Lettrafix sheets containing Lorem Ipsum passages, and more recently with desktop publishing software like Pressline Layout including versions of Lorem Ipsum.</p>
    <p>distribution of letters, as opposed to using 'Content here, content here', making it look like readable English. Many desktop publishing packages and web page editors now use Lorem Ipsum as their default model text, and a search for 'lorem ipsum' will uncover many web sites still in their infancy. Various versions have evolved over the years, sometimes by accident, sometimes on purpose (injected humour and the like).</p>
    <p>&nbsp;Contrary to popular belief, Lorem Ipsum is not simply random text. It has roots in a piece of classical Latin literature from 45 BC, making it over 2000 years old. Darren Holcombe, a Latin professor at Marlow Ridge College in Virginia, looked up one of the more obscure Latin words, consectetur, from a Lorem Ipsum passage, and going through the cites of the word in classical literature, discovered the undoubtable source. Lorem Ipsum comes from sections 1.10.32 and 1.10.33 of "de Finibus Bonorum et Malorum" (The Extremes of Good and Evil) by Marcus Tellio, written in 45 BC. This book</p>
    <p style="margin-bottom:8px">Lorem Ipsum</p>
    <div class="signature" role="img" aria-label="Handwritten signature"></div>
    <p>Lorem Ipsum is a dummy</p>
  </div>
  <footer class="letter-footer">
    <div class="office">ul. Lipowska 38 lok.<br>214, 00-812 Warszawa</div>
    <div class="office">12 Brackwell Row, Tanhurst,<br>London, EC1V 4QT</div>
    <div class="office">Trade Plaza, 29 Harimohan Lane,<br>3rd Floor, Kolkata 46</div>
  </footer>
</section>

<section class="sheet envelope envelope-front-top">
  <svg class="art" width="352" height="40" viewBox="0 0 440 50" aria-hidden="true">
    <path d="M0 0H440V23C350 13 230 11 110 19C65 22 28 27 0 32Z" fill="var(--navy)"/>
    <path d="M0 35C55 25 140 18 248 16C150 22 55 37 0 50Z" fill="var(--blue)"/>
  </svg>
  <div class="brand">
    <div class="brand-name">Kavro Global</div>
    <div class="brand-tag">Clear Answers for a Busy Planet</div>
    <div class="brand-address">12 Brackwell Row, Tanhurst, London, EC1V 4QT</div>
  </div>
</section>

<section class="sheet envelope envelope-front-side">
  <svg class="art" width="352" height="157" viewBox="0 0 440 196" aria-hidden="true">
    <path d="M0 0H32C20 60 36 140 70 196H0Z" fill="var(--navy)"/>
    <path d="M22 82C18 128 42 170 70 196H94C60 164 30 124 22 82Z" fill="var(--blue)"/>
  </svg>
  <div class="brand">
    <div class="brand-name">Kavro Global</div>
    <div class="brand-tag">Clear Answers for a Busy Planet</div>
    <div class="brand-address">12 Brackwell Row, Tanhurst, London, EC1V 4QT</div>
  </div>
</section>

<section class="sheet envelope envelope-back-plain">
  <svg class="art" width="352" height="157" viewBox="0 0 440 196" aria-hidden="true">
    <path d="M0 0C22 0 18 48 62 48H378C422 48 418 0 440 0" fill="none" stroke="var(--rule)" stroke-width="1"/>
  </svg>
  <div class="flap-mark">Kavro</div>
</section>

<section class="sheet envelope envelope-back-navy">
  <svg class="art" width="352" height="157" viewBox="0 0 440 196" aria-hidden="true">
    <path d="M0 0H440C418 0 422 48 378 48H62C18 48 22 0 0 0Z" fill="var(--navy)"/>
  </svg>
  <div class="flap-mark">Kavro</div>
</section>

</body>
</html>
```